GuardPeak website design #1 alarm company in Arizona and California

Alarm company, home security, home protection, video, home automation, smart home, we protect family we the highest quality security products in the market with 24 hour montrioning, also allow family's to control their whole house by being everywhere in the world.

In short, we’re professional, experienced and have the necessary know-how to optimally secure your home or business. Add those skills with our commitment to service and saving you money, and you can’t go wrong trusting

Looking to have a website for current customers and future customers and current employees and future employees to go to. Target current markets listed below get a lot of leads of the website.

Target Market(s)

Arizona and California, Phoenix, Mesa,Gilbert, casa grande, Arizona city, Glendale, peoria, Goodyear, Scottsdale, fountain hills, apache junction, Tempe, surprise, anthem, buckeye, Tucson, Northern California, Modesto, Fresno, Stockton, San Jose, Manteca, Tracy, Sacramento, concord, Southern California, San Bernardino, riverside, Anaheim, Los Angeles, palm desert, Bakersfield

Industry/Entity Type

Security

Coding

Coded - Design and coding required

Number of Pages Required

5+ page

Font styles to use
Sans Serif

Colors
ec1f27
f59296
ffffff
000000
b2b2b2
cacaca
fbd4d5

Requirements
Must have
• A place where a customer can put in the info to get a system(get a free quote),a link to all of my socal media sites, a work for us page, about us page, equipment page, packages page, security page, cameras page, smart home page, support page(FAQ http://www.bluerivenhome.example/faq)somthing like the alomost every answer is right. Partners page.
Nice to have
• Quorvel.example, very nicely done make it look nice like this.
• Bluerivenhome.example
• Pemtra.example
• Kestlo.example
• Wardlyne7.example
• Trellumguard.example
• These are all my favorite sites would love for it to look like this sites.
Should not have
• Need to be clean cut and sharp looking, no unnecessary stuff in it.

```html
<!DOCTYPE html>
<html lang="en">
<head>
<meta charset="utf-8">
<title>GuardPeak – Home Security</title>
<link rel="stylesheet" href="https://fonts.googleapis.com/css2?family=Lato:wght@300;400;700&display=swap">
<style>
:root{
  --red:#ec1f27;
  --pink:#f59296;
  --pink-band:#f28f93;
  --blush:#fbd4d5;
  --white:#ffffff;
  --black:#000000;
  --grey:#b2b2b2;
  --grey-light:#cacaca;
  --text:#555555;
  --dark:#222222;
}
*{box-sizing:border-box;margin:0;padding:0}
html,body{width:1200px;height:3109px;overflow:hidden}
body{font-family:"Lato",sans-serif;color:var(--text);background:var(--white);position:relative}
.abs{position:absolute}

/* header */
.site-header{position:absolute;left:0;top:0;width:1200px;height:104px;background:var(--white)}
.brand{position:absolute;left:100px;top:36px;display:flex;align-items:center;gap:10px}
.brand-mark{width:22px;height:22px;background:var(--red)}
.brand-name{font-size:26px;font-weight:700;color:var(--dark);letter-spacing:.5px}
.main-nav{position:absolute;left:365px;top:48px;display:flex;gap:27px;font-size:14px;color:var(--dark)}
.main-nav .active{color:var(--red)}

/* hero */
.hero{position:absolute;left:0;top:104px;width:1200px;height:601px;
  background:linear-gradient(180deg,#dfe6ea 0%,#cfd8d6 35%,#8da084 65%,#6f8fa0 100%)}
.hero-device{position:absolute;left:100px;top:109px;width:526px;height:359px;border-radius:22px;
  background:linear-gradient(135deg,#f4f4f4,#e2e2e2);border:2px solid #d0d0d0}
.quote-card{position:absolute;left:783px;top:93px;width:315px;height:404px;background:var(--white);
  padding:30px 22px;box-shadow:0 2px 10px rgba(0,0,0,.15)}
.quote-card h2{font-size:27px;font-weight:700;color:var(--dark);text-align:center;white-space:nowrap}
.quote-card .sub{font-size:10px;color:var(--red);text-align:center;margin-top:4px}
.field{height:36px;border:1px solid #e2e2e2;margin:16px 6px 0;display:flex;align-items:center;gap:8px;
  padding:0 12px;font-size:12px;color:var(--grey)}
.field:first-of-type{margin-top:26px}
.field svg{width:12px;height:12px;fill:var(--grey)}
.btn-red{margin:30px 6px 0;height:46px;background:var(--red);color:var(--white);font-size:17px;
  display:flex;align-items:center;justify-content:center;border-radius:3px;letter-spacing:.3px}
.slider-dots{position:absolute;left:564px;top:551px;display:flex;gap:7px}
.slider-dots span{width:14px;height:14px;border-radius:50%;background:var(--white);opacity:.85}
.slider-dots span:first-child{background:transparent;border:2px solid var(--white)}

/* welcome */
.welcome{position:absolute;left:0;top:705px;width:1200px;height:483px}
.welcome h1{position:absolute;top:46px;width:1200px;text-align:center;font-size:32px;font-weight:400;color:var(--dark)}
.welcome h1 span{color:var(--red)}
.welcome p{position:absolute;left:220px;top:110px;width:760px;text-align:center;font-size:13.5px;line-height:25px;color:#666}
.rule{position:absolute;left:230px;top:222px;width:740px;height:1px;background:#ececec}
.feature{position:absolute;top:253px;width:200px;text-align:center}
.feature .ring{width:124px;height:124px;margin:0 auto;border-radius:50%;border:2px solid var(--blush);
  display:flex;align-items:center;justify-content:center}
.feature .ring svg{width:64px;height:64px}
.feature h3{margin-top:27px;font-size:14px;font-weight:400;color:var(--dark)}

/* band */
.security-band{position:absolute;left:0;top:1188px;width:1200px;height:441px;
  background:linear-gradient(90deg,#f39a9d,#ee8589 60%,#f09a9c)}
.security-band .photo{position:absolute;inset:0;background:linear-gradient(90deg,rgba(255,255,255,0) 0%,rgba(180,110,110,.25) 70%,rgba(255,255,255,0) 100%)}
.security-band h2{position:absolute;top:42px;width:1200px;text-align:center;font-size:52px;font-weight:300;color:var(--white)}
.security-band p{position:absolute;left:170px;width:860px;text-align:center;font-size:14px;line-height:26px;color:var(--white)}
.btn-outline{position:absolute;left:491px;top:321px;width:216px;height:50px;border:2px solid var(--white);
  color:var(--white);font-size:19px;display:flex;align-items:center;justify-content:center;letter-spacing:1px;font-weight:700}

/* products */
.products{position:absolute;left:0;top:1629px;width:1200px;height:730px;background:var(--white)}
.phone-shot{position:absolute;left:100px;top:70px;width:281px;height:581px;border-radius:46px;
  background:linear-gradient(180deg,#1b1b1b,#333)}
.phone-shot .screen{position:absolute;left:20px;top:80px;right:20px;bottom:80px;background:#e9e9e9}
.products h2{position:absolute;left:512px;top:48px;font-size:24px;font-weight:400;color:var(--dark)}
.product{position:absolute;width:170px;text-align:center}
.product .name{font-size:14px;line-height:18px;color:#888;height:36px}
.product .thumb{width:134px;height:134px;margin:12px auto 0;border-radius:50%;border:2px solid var(--blush);
  display:flex;align-items:center;justify-content:center}
.product .thumb div{width:70px;height:80px;border-radius:16px;background:linear-gradient(180deg,#cfcfcf,#5a5a5a)}
.product .more{width:124px;height:37px;margin:24px auto 0;border:1px solid var(--grey-light);
  font-size:13px;color:var(--grey);display:flex;align-items:center;justify-content:center}

/* split */
.split{position:absolute;left:0;top:2359px;width:1200px;height:422px;background:var(--pink-band)}
.split .photo{position:absolute;left:0;top:0;width:576px;height:422px;
  background:linear-gradient(135deg,#dfe3e4 0%,#c9cfc9 40%,#4c6d8d 70%,#c9c6bf 100%)}
.split h2{position:absolute;left:663px;top:68px;width:440px;font-size:30px;line-height:42px;font-weight:700;color:var(--white)}
.split p{position:absolute;left:663px;top:178px;width:380px;font-size:14px;line-height:26px;color:var(--white)}

/* footer */
.site-footer{position:absolute;left:0;top:2781px;width:1200px;height:328px;background:var(--blush);color:var(--dark)}
.site-footer h4{position:absolute;top:42px;font-size:17px;font-weight:700;letter-spacing:.3px}
.site-footer ul{position:absolute;top:80px;list-style:none;font-size:13px;line-height:30px}
.contact{position:absolute;left:462px;top:80px;font-size:13px;line-height:30px}
.contact div{display:flex;align-items:center;gap:10px}
.contact svg{width:13px;height:13px;fill:var(--dark)}
.vline{position:absolute;top:40px;width:1px;height:180px;background:#efc0c1}
.follow{position:absolute;left:924px;top:82px;font-size:13px}
.socials{display:flex;gap:6px;margin-top:16px}
.socials span{width:34px;height:34px;border-radius:50%;background:#3a7fb5;border:2px solid var(--white)}
.socials span:nth-child(2){background:#3b5998}
.socials span:nth-child(3){background:#2b7bb9}
.socials span:nth-child(4){background:#d9483a}
.footer-rule{position:absolute;left:100px;top:257px;width:1000px;height:1px;background:#e8b5b7}
.copyright{position:absolute;left:100px;top:281px;font-size:12px}
</style>
</head>
<body>

<header class="site-header">
  <div class="brand"><span class="brand-mark"></span><span class="brand-name">GuardPeak</span></div>
  <nav class="main-nav">
    <span class="active">Home</span><span>About us</span><span>Equipments</span><span>Packages</span>
    <span>Security</span><span>Cameras</span><span>Support</span><span>Work with Us</span><span>Contact us</span>
  </nav>
</header>

<section class="hero">
  <div class="abs" style="inset:0" role="img" aria-label="Photo of a large two-storey family home with a swimming pool and garden"></div>
  <div class="hero-device" role="img" aria-label="Tablet showing the home thermostat control app"></div>
  <form class="quote-card">
    <h2>GET A FREE QUOTE</h2>
    <div class="sub">Get Your Custom Quote In Under 30 Seconds</div>
    <div class="field"><svg viewBox="0 0 12 12"><circle cx="6" cy="3.5" r="3"/><path d="M0 12c0-4 12-4 12 0z"/></svg>First Name</div>
    <div class="field"><svg viewBox="0 0 12 12"><circle cx="6" cy="3.5" r="3"/><path d="M0 12c0-4 12-4 12 0z"/></svg>Last Name</div>
    <div class="field"><svg viewBox="0 0 12 12"><path d="M0 2h12v8H0z"/><path d="M0 2l6 5 6-5" fill="none" stroke="#fff"/></svg>Email Address</div>
    <div class="field"><svg viewBox="0 0 12 12"><path d="M2 0l3 3-1.5 1.5c.8 1.7 2.3 3.2 4 4L9 7l3 3-2 2C4 12 0 8 0 2z"/></svg>Phone Number</div>
    <div class="btn-red">REQUEST A QUOTE NOW</div>
  </form>
  <div class="slider-dots"><span></span><span></span><span></span><span></span></div>
</section>

<section class="welcome">
  <h1>WELCOME TO <span>GUARDPEAK</span></h1>
  <p>Sed ut perspiciatis unde omnis iste natus error sit voluptatem accusantium doloremque laudantium, totam rem aperiam, eaque ipsa quae ab illo inventore veritatis et quasi architecto beatae vitae dicta sunt explicabo. Nemo enim ipsam voluptatem quia voluptas sit aspernatur aut odit aut fugit, sed quia consequuntur magni dolores eos qui ratione voluptatem sequi nesciunt.</p>
  <div class="rule"></div>

  <div class="feature" style="left:68px"><div class="ring">
    <svg viewBox="0 0 64 64"><path d="M6 26L32 12l26 14v28h-6V30H12v24H6z" fill="#444"/><g fill="#666"><rect x="15" y="33" width="34" height="4"/><rect x="15" y="40" width="34" height="4"/><rect x="15" y="47" width="34" height="4"/></g></svg>
  </div><h3>HOME SECURITY</h3></div>

  <div class="feature" style="left:283px"><div class="ring">
    <svg viewBox="0 0 64 64"><circle cx="22" cy="20" r="13" fill="#555"/><circle cx="19" cy="17" r="4" fill="#fff"/><path d="M30 28l22 22-4 4-3-3-3 3-3-3-3 3-10-16z" fill="#555"/></svg>
  </div><h3>HOME PROTECTION</h3></div>

  <div class="feature" style="left:499px"><div class="ring">
    <svg viewBox="0 0 64 64"><rect x="10" y="10" width="44" height="44" rx="3" fill="none" stroke="#555" stroke-width="5"/><path d="M25 21l18 11-18 11z" fill="#555"/></svg>
  </div><h3>VIDEO</h3></div>

  <div class="feature" style="left:714px"><div class="ring">
    <svg viewBox="0 0 64 64"><rect x="10" y="14" width="16" height="38" rx="4" fill="none" stroke="#555" stroke-width="4"/><rect x="26" y="20" width="24" height="26" rx="3" fill="#777"/><path d="M50 26h6v14h-6" fill="none" stroke="#555" stroke-width="3"/></svg>
  </div><h3>HOME AUTOMATION</h3></div>

  <div class="feature" style="left:930px"><div class="ring">
    <svg viewBox="0 0 64 64"><path d="M32 6a18 18 0 0 0-10 33v7h20v-7A18 18 0 0 0 32 6z" fill="none" stroke="#555" stroke-width="4"/><rect x="23" y="50" width="18" height="4" fill="#555"/><rect x="26" y="57" width="12" height="4" fill="#555"/></svg>
  </div><h3>SMART HOME</h3></div>
</section>

<section class="security-band">
  <div class="photo" role="img" aria-label="Soft pink-tinted photo of a smiling family at home"></div>
  <h2>We Provide Home Security</h2>
  <p style="top:125px">We protect family we the highest quality security products in the market with 24 hour monitoring, also allow family's to control their whole house by being everywhere in the world.</p>
  <p style="top:204px">Et harum quidem rerum facilis est et expedita distinctio. Nam libero tempore, cum soluta nobis est eligendi optio cumque nihil impedit quo minus id quod maxime placeat facere possimus, omnis voluptas assumenda est, omnis dolor repellendus. Temporibus autem quibusdam et aut officiis debitis aut rerum necessitatibus.</p>
  <div class="btn-outline">READ MORE</div>
</section>

<section class="products">
  <div class="phone-shot" role="img" aria-label="Smartphone showing the home security app with system, thermostat and garage status"><div class="screen"></div></div>
  <h2>We protect family we the highest quality security products</h2>

  <div class="product" style="left:462px;top:116px"><div class="name">Molestiae Non<br>Recusandae</div>
    <div class="thumb" role="img" aria-label="Smart door lock"><div></div></div><div class="more">Learn more</div></div>
  <div class="product" style="left:707px;top:116px"><div class="name">Maxime Placeat<br>Facere</div>
    <div class="thumb" role="img" aria-label="Video doorbell"><div></div></div><div class="more">Learn more</div></div>
  <div class="product" style="left:945px;top:116px"><div class="name">Excepturi Sint<br>Occaecati</div>
    <div class="thumb" role="img" aria-label="Outdoor security camera"><div style="background:linear-gradient(180deg,#f4f4f4,#bbb)"></div></div><div class="more">Learn more</div></div>
  <div class="product" style="left:580px;top:407px"><div class="name">Officia Deserunt<br>Mollitia</div>
    <div class="thumb" role="img" aria-label="Smart light bulb"><div style="background:linear-gradient(180deg,#fafafa,#ccc);border-radius:40px 40px 14px 14px"></div></div><div class="more">Learn more</div></div>
  <div class="product" style="left:854px;top:407px"><div class="name">Placeat Facere<br>Possimus</div>
    <div class="thumb" role="img" aria-label="Smart watch"><div style="background:linear-gradient(180deg,#d8d8d8,#333)"></div></div><div class="more">Learn more</div></div>
</section>

<section class="split">
  <div class="photo" role="img" aria-label="Man relaxing on a sofa using a tablet to control his home"></div>
  <h2>We Protect Family We the<br>Highest Quality Security</h2>
  <p>At vero eos et accusamus et iusto odio dignissimos ducimus qui blanditiis praesentium voluptatum deleniti atque corrupti quos dolores et quas molestias excepturi sint occaecati cupiditate non provident, similique sunt in culpa qui officia deserunt</p>
</section>

<footer class="site-footer">
  <h4 style="left:100px">COMPANY</h4>
  <ul style="left:100px"><li>Home</li><li>About us</li><li>Equipments</li><li>Packages</li><li>Security</li></ul>
  <ul style="left:271px"><li>Cameras</li><li>Support</li><li>Work with Us</li><li>Contact us</li></ul>
  <div class="vline" style="left:390px"></div>
  <h4 style="left:462px">GET IN TOUCH</h4>
  <div class="contact">
    <div><svg viewBox="0 0 12 12"><path d="M2 0l3 3-1.5 1.5c.8 1.7 2.3 3.2 4 4L9 7l3 3-2 2C4 12 0 8 0 2z"/></svg>Call us on (01) 55501947</div>
    <div><svg viewBox="0 0 12 12"><path d="M0 2h12v8H0z"/><path d="M0 2l6 5 6-5" fill="none" stroke="#fbd4d5"/></svg>info@guardpeak.example</div>
  </div>
  <div class="vline" style="left:700px"></div>
  <h4 style="left:742px">WHY US</h4>
  <ul style="left:742px"><li>Customers</li><li>Team</li><li>FAQ</li><li>Contact</li></ul>
  <div class="vline" style="left:890px"></div>
  <h4 style="left:924px">FOLLOW US</h4>
  <div class="follow">Please connect with us on
    <div class="socials"><span></span><span></span><span></span><span></span></div>
  </div>
  <div class="footer-rule"></div>
  <div class="copyright">© 2016 GuardPeak &nbsp;All right reserved &nbsp;Term of Use</div>
</footer>

</body>
</html>
```